CBD oil label, sleek, clean, serious

I need graphic design for a CBD oil company. Black and white labels for 30ml amber color dropper bottles. looking for something that stands out in its simplicity. this product will be a top of the line, highest margin due to quality of ingredients. It should look rich. other products on the shelf use a lot of color and logos. this label should be clear and stand out as a place to rest your eyes in a sea of marketing glitz.

please see the idea board.

Target Market(s)

middle to older adults

Industry/Entity Type

Health And Wellness

Font styles to use
Serif

Colors
fff5ef
cadf82

Requirements
Must have
• We want the look of elegance and like an apothecary label
• Product name will be VelmoraSharp or VelmoraEase
• see other details on the attached idea board
Nice to have
• think Duvrelle and old style apothecary with a modern aesthetic
Should not have
• any reference or drawing of cannabis

```html
<!DOCTYPE html>
<html lang="en">
<head>
<meta charset="utf-8">
<title>VelmoraEase Full Spectrum CBD Oil – Packaging</title>
<link href="https://fonts.googleapis.com/css2?family=Rubik:wght@400;500;700&family=Roboto:wght@400&display=swap" rel="stylesheet">
<style>
  :root {
    --bg: #e3e3e3;
    --box-light: #f4f4f4;
    --box-grey: #c6c6c6;
    --label-cream: #faf8f0;
    --label-edge: #cfd0d2;
    --ink: #151515;
    --ink-soft: #3a3a3a;
    --pill: #cfcfcf;
  }
  * { box-sizing: border-box; margin: 0; padding: 0; }
  html, body { width: 1200px; height: 800px; overflow: hidden; }
  body {
    background: var(--bg);
    font-family: "Rubik", Arial, sans-serif;
    color: var(--ink);
    position: relative;
  }

  /* Carton front */
  .carton {
    position: absolute; left: 60px; top: 118px; width: 236px; height: 560px;
    background: var(--box-light); text-align: center;
  }
  .carton-lower {
    position: absolute; left: 0; right: 0; top: 312px; bottom: 0; background: var(--box-grey);
  }
  .carton .brand { position: absolute; top: 112px; width: 100%; font-size: 19px; letter-spacing: 2px; }
  .carton .spectrum { position: absolute; top: 214px; width: 100%; font-size: 14px; letter-spacing: 1.5px; }
  .carton .oil { position: absolute; top: 232px; width: 100%; font-size: 29px; font-weight: 700; letter-spacing: 2px; }
  .carton .flavor { position: absolute; top: 274px; width: 100%; font-size: 13px; letter-spacing: 1px; }
  .carton .product { position: absolute; top: 378px; width: 100%; font-size: 27px; font-weight: 700; color: #2a2a2a; letter-spacing: 1px; }
  .carton .volume { position: absolute; top: 518px; width: 100%; font-size: 13px; font-weight: 500; letter-spacing: 1px; }

  /* Flat wrap label */
  .wrap-label {
    position: absolute; left: 367px; top: 82px; width: 290px; height: 610px;
    background: var(--label-cream);
    border-left: 8px solid var(--label-edge);
    border-right: 12px solid var(--label-edge);
  }
  .directions {
    position: absolute; left: 10px; top: 44px; width: 244px;
    transform: rotate(180deg);
    font-family: "Roboto", Arial, sans-serif; font-size: 7.6px; line-height: 11.5px; color: var(--ink-soft);
  }
  .directions p + p { margin-top: 10px; }

  /* Rotated run: x runs bottom-to-top, y runs left-to-right */
  .label-run {
    position: absolute; left: 0; top: 600px; width: 380px; height: 270px;
    transform-origin: top left; transform: rotate(-90deg);
  }
  .label-run .line { position: absolute; white-space: nowrap; line-height: 1; }
  .facts {
    position: absolute; left: 12px; top: 40px; width: 130px;
    font-family: "Roboto", Arial, sans-serif; font-size: 7.6px; line-height: 10px; color: var(--ink-soft);
  }
  .facts p + p { margin-top: 18px; }
  .storage { position: absolute; left: 12px; top: 222px; font-family: "Roboto", Arial, sans-serif; font-size: 7.6px; line-height: 1; color: var(--ink-soft); }
  .marks { position: absolute; left: 18px; top: 240px; display: flex; gap: 18px; }
  .mark { display: flex; flex-direction: column; align-items: center; gap: 2px; width: 12px; font-family: "Roboto", Arial, sans-serif; font-size: 3.5px; color: var(--ink-soft); white-space: nowrap; }
  .mark .dot { width: 12px; height: 12px; border: 1px solid var(--ink-soft); border-radius: 50%; }
  .run-brand { font-size: 14px; letter-spacing: 1.5px; left: 246px; top: 44px; }
  .run-product { font-size: 21px; font-weight: 700; left: 222px; top: 98px; }
  .run-spectrum { font-size: 11px; letter-spacing: 1px; left: 238px; top: 145px; }
  .run-oil { font-size: 22px; font-weight: 700; letter-spacing: 1.5px; left: 235px; top: 162px; }
  .run-flavor { font-size: 10.5px; letter-spacing: .5px; left: 259px; top: 193px; }
  .run-pill {
    position: absolute; left: 231px; top: 246px; width: 123px; height: 24px;
    background: var(--pill); border-radius: 12px 12px 0 0;
    font-size: 10px; font-weight: 500; text-align: center; line-height: 24px; letter-spacing: .5px;
  }

  /* Bottle front label */
  .front-label {
    position: absolute; left: 745px; top: 438px; width: 150px; height: 232px;
    background: #f6f6f6; text-align: center; overflow: hidden;
  }
  .front-label .brand { margin-top: 30px; font-size: 12px; letter-spacing: 1.5px; }
  .front-label .product { margin-top: 30px; font-size: 17px; font-weight: 700; }
  .front-label .spectrum { margin-top: 18px; font-size: 9.5px; letter-spacing: 1px; }
  .front-label .oil { font-size: 19px; font-weight: 700; letter-spacing: 1.5px; }
  .front-label .flavor { font-size: 9px; letter-spacing: .5px; }
  .front-label .band { position: absolute; left: 0; bottom: 0; width: 150px; height: 40px; }
  .front-label .volume { position: absolute; bottom: 14px; width: 100%; font-size: 9px; font-weight: 500; letter-spacing: .5px; }
</style>
</head>
<body>

<section class="carton" aria-label="Carton front">
  <div class="carton-lower"></div>
  <p class="brand">ORRIN VALE</p>
  <p class="spectrum">FULL SPECTRUM</p>
  <p class="oil">CBD OIL</p>
  <p class="flavor">Mint flavor</p>
  <p class="product">VelmoraEase</p>
  <p class="volume">30 ml &nbsp;|&nbsp; 1000 mg</p>
</section>

<section class="wrap-label" aria-label="Bottle wrap label">
  <div class="directions">
    <p>Use: Shake well. Take 1 dropper to the mark twice daily.<br>Hold under the tongue for 30 seconds. Use every day for<br>best results. Start CBD use with a half dose and work up to<br>full dose after 7 days.</p>
    <p>Discuss CBD use with a physician if taking other<br>medications. Do not exceed 5 doses in a day</p>
  </div>
  <div class="label-run">
    <div class="facts">
      <p>Food Supplement Contains:<br>Full Spectrum CBD,<br>Hemp oil and Natural flavor</p>
      <p>CBD derived from Cannabis<br>less than 0.025 THC</p>
      <p>Derived from Cannabis<br>as a full spectrum oil</p>
    </div>
    <p class="storage">Store in a cool, dark place</p>
    <div class="marks">
      <div class="mark"><span class="dot"></span>Vegan</div>
      <div class="mark"><span class="dot"></span>Non GMO</div>
      <div class="mark"><span class="dot"></span>Pure CBD</div>
      <div class="mark"><span class="dot"></span>Natural</div>
    </div>
    <p class="line run-brand">ORRIN VALE</p>
    <p class="line run-product">VelmoraEase</p>
    <p class="line run-spectrum">FULL SPECTRUM</p>
    <p class="line run-oil">CBD OIL</p>
    <p class="line run-flavor">Mint flavor</p>
    <div class="run-pill">30 ml &nbsp;|&nbsp; 1000 mg</div>
  </div>
</section>

<section class="front-label" aria-label="Bottle front label">
  <p class="brand">ORRIN VALE</p>
  <p class="product">VelmoraEase</p>
  <p class="spectrum">FULL SPECTRUM</p>
  <p class="oil">CBD OIL</p>
  <p class="flavor">Mint flavor</p>
  <svg class="band" viewBox="0 0 150 40" aria-hidden="true">
    <path d="M0 28 Q75 18 150 28 V40 H0 Z" fill="#c9c9c9"/>
    <path d="M28 30 V12 Q28 4 36 4 H114 Q122 4 122 12 V30 Z" fill="#d3d3d3"/>
  </svg>
  <p class="volume">30 ml &nbsp;|&nbsp; 1000 mg</p>
</section>

</body>
</html>
```